Marlow 2400 - KR Layouts
Harold Pinkney
Project: Marlow 2400 - KR Layouts
Creative Brief
Printing
Banks and Credit Unions, Corporate, would appeal to their customers.
1) Each designer should submit 3 different designs under the category "Customer Appreciation." Visit this page to see past designs: http://www.marlow2400.example/exclusive-images/customer-appreciation/. The designs can share comment graphical elements (such as color scheme or layout), but must be different. 2) Please use pixavane.example as your image source (just download the comp image and we will purchase the final image once design is complete). 3) Size = 3.125"w x 7"h 4) No bleeds 5) You can use your own copy or reuse some that are on the http://www.marlow2400.example/exclusive-images/customer-appreciation/.

```html
<!DOCTYPE html>
<html lang="en">
<head>
<meta charset="utf-8">
<title>Customer Appreciation Banners</title>
<link rel="stylesheet" href="https://fonts.googleapis.com/css2?family=Sofia&family=Comfortaa:wght@300&family=Gelasio&display=swap">
<style>
  :root{
    --stage:#222223;
    --card:#ffffff;
    --blue-light:#2a9be0;
    --blue-dark:#1b52ae;
    --green:#3d8c1c;
    --green-dark:#1d6b2c;
    --red:#c21f2d;
    --red-dark:#7c0f1a;
    --ink-light:#ffffff;
  }
  html,body{margin:0;padding:0;width:1200px;height:901px;overflow:hidden;background:var(--stage);}
  .stage{position:relative;width:1200px;height:901px;}
  .banner{position:absolute;top:122px;width:319px;height:640px;background:var(--card);overflow:hidden;}
  .banner--blue{left:71px;}
  .banner--green{left:448px;}
  .banner--red{left:820px;}
  .banner__photo{position:absolute;left:5px;top:5px;width:309px;}
  .banner--blue .banner__photo{height:222px;background:linear-gradient(180deg,#e9ecef 0%,#cfd4da 45%,#b9a48e 75%,#8c7a66 100%);}
  .banner--green .banner__photo{height:190px;background:linear-gradient(160deg,#b8b2a6 0%,#6d5b4a 40%,#3a3232 70%,#8f7a66 100%);}
  .banner--red .banner__photo{height:195px;background:linear-gradient(170deg,#f2f2ef 0%,#d9d6cf 40%,#8d8f98 75%,#6d6460 100%);}
  .banner__band{position:absolute;left:0;top:0;width:319px;height:640px;}
  .tagline{position:absolute;left:0;width:319px;text-align:center;color:var(--ink-light);margin:0;line-height:1;}
  .tagline--script{font-family:"Sofia",cursive;}
  .tagline--rounded{font-family:"Comfortaa",sans-serif;font-weight:300;}
  .tagline--serif{font-family:"Gelasio",serif;}
</style>
</head>
<body>
<div class="stage">

  <section class="banner banner--blue">
    <div class="banner__photo" role="img" aria-label="Photo of three business people reviewing papers at a desk"></div>
    <svg class="banner__band" viewBox="0 0 319 640" aria-hidden="true">
      <defs>
        <linearGradient id="blueBand" x1="0" y1="0" x2="1" y2="1">
          <stop offset="0" stop-color="var(--blue-light)"/>
          <stop offset="1" stop-color="var(--blue-dark)"/>
        </linearGradient>
      </defs>
      <path d="M5,224 C100,206 210,226 314,198 L314,366 C220,342 120,330 5,330 Z" fill="url(#blueBand)"/>
    </svg>
    <p class="tagline tagline--script" style="top:240px;font-size:30px;">Customer Service</p>
    <p class="tagline tagline--script" style="top:282px;font-size:30px;">is our <span style="font-size:38px;">priority</span></p>
  </section>

  <section class="banner banner--green">
    <div class="banner__photo" role="img" aria-label="Photo of a couple shaking hands with an advisor at a desk"></div>
    <svg class="banner__band" viewBox="0 0 319 640" aria-hidden="true">
      <path d="M5,190 L314,190 L314,298 L160,342 L5,305 Z" fill="var(--green)"/>
      <path d="M5,190 L90,190 L5,222 Z" fill="var(--green-dark)"/>
      <path d="M5,282 L70,290 L5,305 Z" fill="var(--green-dark)"/>
    </svg>
    <p class="tagline tagline--rounded" style="top:224px;font-size:27px;">Customer Service</p>
    <p class="tagline tagline--rounded" style="top:256px;font-size:27px;">is our <span style="font-size:32px;">priority</span></p>
  </section>

  <section class="banner banner--red">
    <div class="banner__photo" role="img" aria-label="Photo of a couple meeting a consultant in a bright office"></div>
    <svg class="banner__band" viewBox="0 0 319 640" aria-hidden="true">
      <path d="M5,300 C90,318 200,330 314,296 L314,332 C210,350 100,338 5,330 Z" fill="var(--red-dark)"/>
      <path d="M5,200 C100,188 210,206 314,192 L314,300 C200,330 90,318 5,304 Z" fill="var(--red)"/>
    </svg>
    <p class="tagline tagline--serif" style="top:228px;font-size:28px;">Customer Service</p>
    <p class="tagline tagline--serif" style="top:260px;font-size:28px;">is our <span style="font-size:33px;">priority</span></p>
  </section>

</div>
</body>
</html>
```